Cedarfield Supply METAL business card

A metal business card design. Attached are older designs for a reference, but we want a NEW design, not the same as in the past. See the 2 examples just posted. We would like some cut out in the design. Possibly the pine cone or the pine tree branch (see image IMG_0).

Target Market(s)

Home and Gardern

Industry/Entity Type

Landscape

Contact Information for Business Card

Logo, website, address, name, phone numbers

```html
<!DOCTYPE html>
<html lang="en">
<head>
<meta charset="utf-8">
<title>Cedarfield Supply – Business Card</title>
<link href="https://fonts.googleapis.com/css2?family=Montserrat:wght@400;500;700&display=swap" rel="stylesheet">
<style>
  :root {
    --stage: #2e2825;
    --card: #262626;
    --orange: #f3911f;
    --white: #f2f2f2;
    --grey-light: #e4e4e4;
    --needle: #8c8c8c;
    --needle-soft: #5a5a5a;
  }
  * { box-sizing: border-box; margin: 0; padding: 0; }
  html, body {
    width: 1200px; height: 786px; overflow: hidden;
    background: var(--stage);
    font-family: "Montserrat", sans-serif;
  }
  .sheet {
    position: relative; width: 1200px; height: 786px;
    display: flex; align-items: center; justify-content: center; gap: 40px;
  }
  .card {
    position: relative; width: 540px; height: 309px;
    background: var(--card); overflow: hidden;
    box-shadow: 0 10px 24px rgba(0,0,0,.35);
  }

  /* contact side */
  .card-back .grass-art {
    position: absolute; left: 60px; right: 0; bottom: 0; height: 140px;
    background: linear-gradient(to top, var(--needle-soft) 0%, rgba(90,90,90,.55) 45%, rgba(38,38,38,0) 100%);
    clip-path: polygon(0 100%, 0 60%, 15% 30%, 35% 45%, 55% 10%, 75% 25%, 100% 0, 100% 100%);
    opacity: .8;
  }
  .card-back .bands { position: absolute; left: 0; bottom: 0; width: 540px; height: 60px; }
  .card-back .brand {
    position: absolute; left: 30px; top: 128px; width: 200px;
    display: flex; align-items: center; gap: 10px;
  }
  .brand-dot {
    width: 18px; height: 18px; border-radius: 50%; background: var(--orange); flex: none;
  }
  .brand-name {
    color: var(--orange); font-weight: 700; font-size: 20px; line-height: 1.15;
  }
  .divider {
    position: absolute; left: 250px; top: 58px; width: 2px; height: 168px;
    background: var(--orange);
  }
  .contact { position: absolute; left: 272px; top: 62px; color: var(--white); }
  .contact-name {
    color: var(--orange); font-weight: 700; font-size: 21px; margin-bottom: 18px;
  }
  .contact-address { font-size: 12.5px; line-height: 1.35; margin-bottom: 16px; }
  .contact-line {
    display: flex; align-items: center; gap: 10px; font-size: 12.5px; margin-bottom: 9px;
  }
  .contact-line svg { width: 14px; height: 14px; flex: none; }

  /* brand side */
  .card-front .branch-art {
    position: absolute; left: 70px; top: 0; right: 0; bottom: 0;
    background: radial-gradient(ellipse at 60% 48%, rgba(160,160,160,.7) 0%, rgba(140,140,140,.4) 40%, rgba(38,38,38,0) 75%);
    clip-path: polygon(0 55%, 30% 20%, 55% 0, 85% 5%, 100% 40%, 90% 80%, 60% 100%, 25% 90%);
  }
  .card-front .cone-cutout {
    position: absolute; left: 355px; top: 55px; width: 70px; height: 70px;
    border-radius: 50%; background: var(--stage);
    box-shadow: inset 0 0 0 2px rgba(255,255,255,.15);
  }
  .card-front .brand {
    position: absolute; left: 150px; top: 130px;
    display: flex; align-items: center; gap: 12px;
  }
  .card-front .brand-dot { width: 26px; height: 26px; }
  .card-front .brand-name { font-size: 34px; }
</style>
</head>
<body>
<main class="sheet">

  <section class="card card-back" aria-label="Business card, contact side">
    <div class="grass-art" role="img" aria-label="Sketched pine straw blades rising along the bottom edge"></div>
    <svg class="bands" viewBox="0 0 540 60" aria-hidden="true">
      <polygon points="0,47 380,47 374,60 0,60" fill="var(--orange)"/>
      <polygon points="386,22 540,22 540,60 370,60" fill="var(--grey-light)"/>
    </svg>

    <div class="brand">
      <span class="brand-dot"></span>
      <span class="brand-name">Cedarfield Supply</span>
    </div>

    <div class="divider"></div>

    <div class="contact">
      <p class="contact-name">Dana Whitlock</p>
      <p class="contact-address">48 Birch Hollow Road<br>Canton, MS 39046</p>
      <p class="contact-line">
        <svg viewBox="0 0 16 16" aria-hidden="true"><path fill="var(--orange)" d="M2 6c0-2 3-3.5 6-3.5S14 4 14 6v1.5h-3V6H5v1.5H2zM4 8h8l1 6H3z"/></svg>
        888.555.0142
      </p>
      <p class="contact-line">
        <svg viewBox="0 0 16 16" aria-hidden="true"><rect x="4" y="1" width="8" height="14" rx="1.5" fill="none" stroke="var(--orange)" stroke-width="1.6"/><circle cx="8" cy="12.5" r="0.9" fill="var(--orange)"/></svg>
        601.555.0187
      </p>
      <p class="contact-line">
        <svg viewBox="0 0 16 16" aria-hidden="true"><circle cx="8" cy="8" r="6.5" fill="none" stroke="var(--orange)" stroke-width="1.5"/><path d="M1.5 8h13M8 1.5c-3 3.5-3 9.5 0 13M8 1.5c3 3.5 3 9.5 0 13" fill="none" stroke="var(--orange)" stroke-width="1.2"/></svg>
        www.cedarfieldsupply.com
      </p>
    </div>
  </section>

  <section class="card card-front" aria-label="Business card, brand side">
    <div class="branch-art" role="img" aria-label="Grey sketch of a pine branch spreading across the card, cut out of the metal"></div>
    <div class="cone-cutout" role="img" aria-label="Pine cone cut-out in the metal"></div>
    <div class="brand">
      <span class="brand-dot"></span>
      <span class="brand-name">Cedarfield Supply</span>
    </div>
  </section>

</main>
</body>
</html>
```